Need Modern Elegant Professional Invoice Design

Need modern elegant professional invoice design along with a second page for time and expense log for professional services

```html
<!DOCTYPE html>
<html lang="en">
<head>
<meta charset="utf-8">
<title>Northline Adjusters – Invoice and Time &amp; Expense Log</title>
<link href="https://fonts.googleapis.com/css2?family=Roboto:wght@400;500;700&display=swap" rel="stylesheet">
<style>
  :root{
    --bg:#e9e2d6;
    --paper:#ffffff;
    --orange:#f47f20;
    --purple:#3a17a8;
    --ink:#222222;
    --muted:#555555;
    --cell:#ebeced;
    --rule:#8a8a8a;
  }
  *{box-sizing:border-box;margin:0;padding:0}
  html,body{width:1200px;height:821px;overflow:hidden}
  body{background:var(--bg);font-family:"Roboto",Arial,sans-serif;color:var(--ink);position:relative}

  .page{position:absolute;top:94px;width:487px;height:630px;background:var(--paper);box-shadow:0 8px 18px rgba(0,0,0,.25)}
  .page--invoice{left:73px}
  .page--log{left:649px}

  .brand{position:absolute;left:26px;top:38px;display:flex;align-items:center;gap:7px}
  .brand__dot{width:14px;height:14px;border-radius:50%;background:var(--orange)}
  .brand__name{font-size:21px;font-weight:700;color:var(--purple);letter-spacing:1px}

  .meta{position:absolute;left:340px;top:31px;font-size:9.5px;line-height:15px;color:var(--muted)}
  .meta b{font-weight:500;color:var(--purple)}
  .meta .meta__no b{color:var(--orange)}
  .meta .meta__no span{color:var(--muted);font-weight:500}

  .title-band{position:absolute;left:0;top:98px;width:223px;height:45px}
  .title-band svg{position:absolute;inset:0}
  .title-band h1{position:absolute;left:23px;top:2px;font-size:39px;line-height:41px;font-weight:500;color:#fff;letter-spacing:.5px;white-space:nowrap}

  .bill-to{position:absolute;left:340px;top:93px;font-size:9.5px;line-height:10.8px;color:var(--muted)}
  .bill-to h2{font-size:13px;font-weight:500;color:var(--orange);margin-bottom:3px}
  .bill-to .bill-to__name{font-weight:700;color:var(--purple)}

  .items{position:absolute;left:35px;top:182px;width:416px;border-collapse:collapse;font-size:9.5px}
  .items th{background:var(--purple);color:#fff;font-weight:500;height:30px;text-align:left}
  .items td{height:30.6px;border-bottom:1px solid var(--rule)}
  .items tr:last-child td{border-bottom:none}
  .items .c-sl{width:32px;text-align:center}
  .items .c-desc{width:183px;padding-left:20px}
  .items .c-price{width:72px;text-align:center}
  .items .c-qty{width:51px;text-align:center}
  .items .c-total{width:78px;padding-left:20px}
  .items td.c-sl,.items td.c-price,.items td.c-total{background:var(--cell)}

  .log{position:absolute;left:35px;top:182px;width:416px;border-collapse:collapse;font-size:9.5px}
  .log th{background:var(--purple);color:#fff;font-weight:500;height:30px;text-align:center}
  .log th.l-task{text-align:left;padding-left:12px}
  .log td{height:30.6px;border-bottom:1px solid var(--rule);text-align:center}
  .log td.l-task{text-align:left;padding-left:12px}
  .log .l-date{width:62px}
  .log .l-task{width:136px}
  .log .l-hrs{width:44px}
  .log .l-rate{width:56px}
  .log .l-exp{width:56px}
  .log .l-amt{width:62px}
  .log td.l-date,.log td.l-rate,.log td.l-amt{background:var(--cell)}
  .log tr.log__sum td{font-weight:500;border-bottom:none}

  .totals{position:absolute;left:243px;top:444px;width:208px;font-size:9.5px;font-weight:500}
  .totals__row{display:flex;padding-left:20px;height:14px;line-height:14px}
  .totals__row span:first-child{width:131px}
  .totals__row--grand{border-top:1px solid var(--rule);margin-top:3px;padding-top:6px;height:22px}

  .thanks{position:absolute;left:35px;top:471px;font-size:9.5px;color:var(--purple)}

  .payment{position:absolute;left:35px;top:495px;font-size:9px;line-height:12.3px;color:var(--ink)}
  .payment h3,.terms h3{font-size:13px;font-weight:500;color:var(--orange);line-height:15px;white-space:nowrap}
  .payment small{font-size:7.5px}

  .terms{position:absolute;left:35px;top:558px;width:124px;font-size:7.3px;line-height:8.5px}

  .sign{position:absolute;left:363px;top:587px;width:89px;border-top:1px solid var(--rule);text-align:center;font-size:9.5px;font-weight:500;padding-top:3px}
</style>
</head>
<body>

<section class="page page--invoice">
  <div class="brand"><span class="brand__dot"></span><span class="brand__name">NORTHLINE</span></div>
  <div class="meta">
    <div class="meta__no"><b>Invoice#</b> <span>12478</span></div>
    <div><b>Date:</b> 08/04/2021</div>
    <div><b>Time:</b> 12:50PM</div>
  </div>
  <div class="title-band">
    <svg width="223" height="45" viewBox="0 0 223 45"><polygon points="0,0 223,0 202,45 0,45" fill="var(--orange)"/></svg>
    <h1>INVOICE</h1>
  </div>
  <div class="bill-to">
    <h2>Invoice to:</h2>
    <div class="bill-to__name">Marcus Bell</div>
    <div>24 Dummy Street Area,</div>
    <div>Location, Lorem Ipsum</div>
    <div>7892478</div>
  </div>

  <table class="items">
    <thead><tr><th class="c-sl">SL.</th><th class="c-desc">Item Description</th><th class="c-price">Price</th><th class="c-qty">Qty</th><th class="c-total">Total</th></tr></thead>
    <tbody>
      <tr><td class="c-sl">1</td><td class="c-desc">Brand Design</td><td class="c-price">$750.00</td><td class="c-qty">01</td><td class="c-total">$750.00</td></tr>
      <tr><td class="c-sl">2</td><td class="c-desc">Web Design</td><td class="c-price">$300.00</td><td class="c-qty">04</td><td class="c-total">$1200.00</td></tr>
      <tr><td class="c-sl">3</td><td class="c-desc">Brochure Design</td><td class="c-price">$500.00</td><td class="c-qty">02</td><td class="c-total">$1000.00</td></tr>
      <tr><td class="c-sl">4</td><td class="c-desc">E-Book Design</td><td class="c-price">$350.00</td><td class="c-qty">03</td><td class="c-total">$1050.00</td></tr>
      <tr><td class="c-sl">5</td><td class="c-desc">Corporate Identity</td><td class="c-price">$1200.00</td><td class="c-qty">01</td><td class="c-total">$1200.00</td></tr>
      <tr><td class="c-sl">6</td><td class="c-desc">Invoice Design</td><td class="c-price">$600.00</td><td class="c-qty">01</td><td class="c-total">$600.00</td></tr>
      <tr><td class="c-sl"></td><td class="c-desc"></td><td class="c-price"></td><td class="c-qty"></td><td class="c-total"></td></tr>
    </tbody>
  </table>

  <div class="totals">
    <div class="totals__row"><span>Sub Total:</span><span>$5,800.00</span></div>
    <div class="totals__row"><span>Tax:</span><span>0.00%</span></div>
    <div class="totals__row totals__row--grand"><span>Total:</span><span>$5,800.00</span></div>
  </div>

  <p class="thanks">Thank you for your business</p>
  <div class="payment">
    <h3>Payment Info:</h3>
    <div>Account No.&nbsp; 40917362845</div>
    <div>A/C Name:&nbsp;&nbsp;&nbsp; <small>Lorem Ipsum</small></div>
    <div>Bank Details: Add your bank details</div>
  </div>
  <div class="terms">
    <h3>Term and Conditions</h3>
    <p>Lorem Ipsum is simply dummy text of the printing and typesetting industry.</p>
  </div>
  <div class="sign">Authorized Sign</div>
</section>

<section class="page page--log">
  <div class="brand"><span class="brand__dot"></span><span class="brand__name">NORTHLINE</span></div>
  <div class="meta">
    <div class="meta__no"><b>Invoice#</b> <span>12478</span></div>
    <div><b>Date:</b> 08/04/2021</div>
    <div><b>Time:</b> 12:50PM</div>
  </div>
  <div class="title-band">
    <svg width="223" height="45" viewBox="0 0 223 45"><polygon points="0,0 223,0 202,45 0,45" fill="var(--orange)"/></svg>
    <h1>INVOICE</h1>
  </div>
  <div class="bill-to">
    <h2>Invoice to:</h2>
    <div class="bill-to__name">Marcus Bell</div>
    <div>24 Dummy Street Area,</div>
    <div>Location, Lorem Ipsum</div>
    <div>7892478</div>
  </div>

  <table class="log">
    <thead><tr><th class="l-date">Date</th><th class="l-task">Time &amp; Expense Log</th><th class="l-hrs">Hours</th><th class="l-rate">Rate</th><th class="l-exp">Expense</th><th class="l-amt">Amount</th></tr></thead>
    <tbody>
      <tr><td class="l-date">07/05/21</td><td class="l-task">Site Inspection</td><td class="l-hrs">3.0</td><td class="l-rate">$85.00</td><td class="l-exp">$40.00</td><td class="l-amt">$295.00</td></tr>
      <tr><td class="l-date">07/09/21</td><td class="l-task">Damage Assessment</td><td class="l-hrs">4.5</td><td class="l-rate">$85.00</td><td class="l-exp">$0.00</td><td class="l-amt">$382.50</td></tr>
      <tr><td class="l-date">07/14/21</td><td class="l-task">Client Meeting</td><td class="l-hrs">1.5</td><td class="l-rate">$85.00</td><td class="l-exp">$25.00</td><td class="l-amt">$152.50</td></tr>
      <tr><td class="l-date">07/20/21</td><td class="l-task">Report Preparation</td><td class="l-hrs">5.0</td><td class="l-rate">$85.00</td><td class="l-exp">$0.00</td><td class="l-amt">$425.00</td></tr>
      <tr><td class="l-date">07/26/21</td><td class="l-task">Travel &amp; Mileage</td><td class="l-hrs">2.0</td><td class="l-rate">$85.00</td><td class="l-exp">$60.00</td><td class="l-amt">$230.00</td></tr>
      <tr><td class="l-date">08/02/21</td><td class="l-task">Claim Review</td><td class="l-hrs">2.5</td><td class="l-rate">$85.00</td><td class="l-exp">$15.00</td><td class="l-amt">$227.50</td></tr>
      <tr class="log__sum"><td class="l-date"></td><td class="l-task">Total</td><td class="l-hrs">18.5</td><td class="l-rate"></td><td class="l-exp">$140.00</td><td class="l-amt">$1712.50</td></tr>
    </tbody>
  </table>

  <p class="thanks">Thank you for your business</p>
  <div class="payment">
    <h3>Payment Info:</h3>
    <div>Account No.&nbsp; 40917362845</div>
    <div>A/C Name:&nbsp;&nbsp;&nbsp; <small>Lorem Ipsum</small></div>
    <div>Bank Details: Add your bank details</div>
  </div>
  <div class="terms">
    <h3>Term and Conditions</h3>
    <p>Lorem Ipsum is simply dummy text of the printing and typesetting industry.</p>
  </div>
  <div class="sign">Authorized Sign</div>
</section>

</body>
</html>
```